Corporate-Design für Osteopathie-Praxis
Das Corporate Design war sehr gut, Änderungswünsche wurden zügig und exakt umgesetzt. Die Designerin stand auch nach der Siegerehrung immer zur Verfügung und hat weitere kleine Änderungen problemlos vorgenommen. Die Zusammenarbeit war immer angenehm und ist nur zu empfehlen.
Zielgruppe
Wir sind eine neue Osteopathie Praxis mit einem Klientel von Jung bis Alt. Vorwiegend etwas gut situiertere Personen. Es soll daher exklusiv aber auch hip sein, da unser Ziel darin besteht eine sehr moderne und edle Praxis aufzubauen.
Aufgabenstellung
Die Praxis soll den Namen „Lumra“ bekommen. Aus zwei Gründen;
die Praxis befindet sich an der Küste in Kiel. Ich möchte hier eine Verbindung zum Standort schaffen. Zweitens sind in dem Namen „Lumra“ meine Initialen MB sowie die Abkürzung für Osteopathie, ost. , vorhanden. Wenn man diese Ideen in dem Logo wiederfinden könnte, wäre es sehr schön. Die Farben blau, weiß, grau richten sich an den skandinavisch-maritimen Stil dem ich folgen möchte. Ich möchte hierbei aber klassisch (nicht verspielt wie zB mit einem Leuchtturm im Logo), etwas exklusiv und hip sein. Es darf aber auch nicht zu abstrakt sein, sodass auch ältere Kunden den Namen/das Logo lesen können

```html
<!DOCTYPE html>
<html lang="de">
<head>
<meta charset="utf-8">
<title>Lumra – Praxis für Osteopathie · Corporate Design</title>
<link href="https://fonts.googleapis.com/css2?family=Open+Sans:wght@300;400;600;800&display=swap" rel="stylesheet">
<style>
:root{
  --teal:#3e6b80;
  --blue:#9cb4c3;
  --pale:#cad8e1;
  --paper:#ffffff;
  --envelope:#ecedee;
  --grey-text:#8a9aa4;
  --faint:#b9c8d1;
  --ink:#333333;
  --ink-light:#a9a9a9;
  --stage:#ffffff;
}
*{box-sizing:border-box;margin:0;padding:0}
html,body{width:1200px;height:876px;overflow:hidden;background:var(--stage);font-family:"Open Sans",Arial,sans-serif;color:var(--teal)}
.board{position:relative;width:1200px;height:876px}
.item{position:absolute;overflow:hidden;background:var(--paper);box-shadow:0 4px 10px rgba(0,0,0,.12)}
.wordmark{font-weight:400;color:var(--teal);letter-spacing:.06em;line-height:1;white-space:nowrap}
.tagline{font-weight:800;color:var(--teal);letter-spacing:.08em;line-height:1;white-space:nowrap}
.brand{position:absolute;text-align:center}
.brand .tagline{margin-top:3px}
.layer{position:absolute;left:0;top:0}
.spine{position:absolute;border-radius:40% 60% 50% 50%}
.right{text-align:right}
.small{font-size:4.6px;line-height:1.55;color:var(--teal)}

/* vertical card front */
.card-v1{left:34px;top:33px;width:135px;height:208px}
.card-v1 .name{position:absolute;right:10px;top:96px;font-size:9.5px;font-weight:300;line-height:1.35;text-align:right;color:var(--teal)}
.card-v1 .contact{position:absolute;right:10px;top:139px;font-size:4.6px;line-height:2.1;text-align:right}
.card-v1 .web{position:absolute;right:10px;top:188px;font-size:5.6px}

/* vertical card back */
.card-v2{left:34px;top:274px;width:135px;height:210px}
.card-v2 .claim{position:absolute;left:52px;width:66px;top:96px;text-align:center;color:#fff;font-size:7.4px;line-height:1.55;font-weight:400}
.card-v2 .claim b{font-weight:800}
.card-v2 .note{position:absolute;left:52px;width:68px;top:183px;text-align:center;color:#fff;font-size:4.4px;line-height:1.6}

/* letterheads */
.letter{width:317px;height:448px}
.letter-a{left:208px;top:35px}
.letter-b{left:847px;top:36px}
.letter .meta{position:absolute;left:38px;font-size:4.2px;color:var(--teal)}
.letter .body{position:absolute;left:38px;width:222px;font-size:4.7px;line-height:1.5;color:var(--teal)}
.letter .bullet{position:absolute;left:49px;width:212px;font-size:4.7px;line-height:1.5;color:var(--teal)}
.letter .bullet::before{content:"";position:absolute;left:-7px;top:3px;width:3px;height:3px;border-radius:50%;background:var(--teal)}
.letter-b .body,.letter-b .bullet{color:var(--faint)}
.letter-b .bullet::before{background:var(--teal)}
.letter .sign{position:absolute;font-size:4.4px;line-height:1.5}
.letter .sign span{display:block;font-size:5.6px}
.foot{position:absolute;top:386px;width:90px;text-align:center;font-size:4.4px;line-height:1.4;color:var(--teal)}
.foot svg{display:block;margin:0 auto 7px}
.fine{position:absolute;right:22px;top:420px;text-align:right;font-size:2.8px;line-height:2.4;color:var(--grey-text)}
.fine b{color:var(--ink)}
.fold{position:absolute;height:1px;width:14px;background:#999}

/* landscape cards */
.card-h1{left:592px;top:99px;width:225px;height:146px}
.card-h1 .web{position:absolute;left:0;width:100%;top:116px;text-align:center;font-size:7.4px;color:var(--faint);font-weight:300}
.card-h2{left:592px;top:273px;width:225px;height:145px}
.card-h2 .name{position:absolute;right:25px;top:55px;text-align:right;font-variant:small-caps;font-size:9.5px;line-height:1.15;font-weight:300;color:var(--teal)}
.card-h2 .name small{font-size:7.5px;display:block;color:var(--blue)}
.card-h2 .contact{position:absolute;right:25px;top:91px;text-align:right;font-size:5.2px;line-height:2.1;color:var(--faint);font-weight:300}
.card-h2 .icons{position:absolute;right:14px;top:92px;width:7px}
.card-h2 .icons svg{display:block;margin-bottom:3.6px}

/* envelopes */
.env{background:var(--envelope);width:245px;height:122px}
.env-1{left:34px;top:524px}
.env-2{left:306px;top:525px;height:123px}
.env-3{left:648px;top:529px}
.env-4{left:921px;top:528px;width:244px;height:125px}
.window{position:absolute;left:23px;top:61px;width:96px;height:44px;border-radius:5px;background:linear-gradient(115deg,#e6e8ea 55%,#f6f7f8 56%,#f1f2f3 80%);border:1px solid #d6d9dc}
.env .web{position:absolute;font-size:5.4px;color:var(--blue)}
.env-3 .web{color:var(--teal)}
.env-4 .line{position:absolute;left:24px;top:107px;font-size:7.6px;font-weight:800;letter-spacing:.06em;color:var(--teal)}
.env-4 .line span{color:var(--blue);margin-left:6px}

/* primary logos */
.logo-big{position:absolute;top:704px;width:420px;text-align:center}
.logo-big .wordmark{font-size:88px;letter-spacing:.1em;font-weight:400}
.logo-big .tagline{font-size:21.5px;letter-spacing:.1em;margin-top:14px}
.logo-color{left:70px}
.logo-mono{left:674px}
.logo-mono .wordmark,.logo-mono .tagline{color:var(--ink)}
</style>
</head>
<body>
<main class="board">

  <!-- vertical business card, front -->
  <section class="item card-v1">
    <svg class="layer" width="135" height="208" viewBox="0 0 135 208">
      <path d="M0 60 C40 68 90 70 135 58 V208 H0Z" fill="var(--pale)"/>
      <path d="M0 60 C40 68 90 70 135 58 V63 C90 75 40 73 0 66Z" fill="var(--teal)"/>
    </svg>
    <div class="brand" style="left:0;width:135px;top:10px">
      <div class="wordmark" style="font-size:22px">LUMRA</div>
      <div class="tagline" style="font-size:6px">PRAXIS FÜR OSTEOPATHIE</div>
    </div>
    <p class="name">Dr. med.<br>Mirko Behrens</p>
    <p class="contact small">Kiel, Strandweg 12<br>Telefon: +49 431 / 5550123<br>Mobil: +49 170 / 5550124<br>E-Mail: info@lumra-osteopathie.de</p>
    <p class="web small">www.lumra-osteopathie.de</p>
  </section>

  <!-- vertical business card, back -->
  <section class="item card-v2">
    <svg class="layer" width="135" height="210" viewBox="0 0 135 210">
      <path d="M0 60 C40 68 90 70 135 58 V210 H0Z" fill="var(--teal)"/>
      <path d="M0 60 C40 68 90 70 135 58 V63 C90 75 40 73 0 68Z" fill="var(--blue)"/>
    </svg>
    <div class="brand" style="left:0;width:135px;top:12px">
      <div class="wordmark" style="font-size:22px">LUMRA</div>
      <div class="tagline" style="font-size:6px">PRAXIS FÜR OSTEOPATHIE</div>
    </div>
    <div class="spine" role="img" aria-label="Stilisierte Wirbelsäule als helle Dekoration" style="left:12px;top:84px;width:34px;height:112px;background:linear-gradient(180deg,rgba(156,180,195,.55),rgba(156,180,195,.25))"></div>
    <p class="claim">Lassen Sie<br>meine Hände<br>und Ihren Körper<br>ein <b><i>Gespräch</i></b><br>führen!</p>
    <p class="note">Terminvereinbarung bitte telefonisch oder per EMail</p>
  </section>

  <!-- letterhead, version A -->
  <section class="item letter letter-a">
    <div class="brand" style="left:0;width:317px;top:30px">
      <div class="wordmark" style="font-size:25px">LUMRA</div>
      <div class="tagline" style="font-size:6.8px">PRAXIS FÜR OSTEOPATHIE</div>
    </div>
    <p class="meta" style="top:106px">Betreff:</p>
    <p class="meta" style="top:120px">Sehr geehrte/er</p>
    <p class="body" style="top:134px">Lorem ipsum dolor sit amet, consectetur adipiscing elit. Sed ante tortor, rutrum sit amet diam eu, aliquet malesuada eros. Quisque dignissim tortor non purus fringilla finibus. Pellentesque nec dolor augue. Donec vestibulum magna est, sed maximus arcu accumsan a. Donec lacus nisl, dignissim a tempor sed, euismod faucibus dolor.</p>
    <p class="bullet" style="top:186px">Lorem ipsum dolor sit amet, consectetur adipiscing elit. Sed ante tortor, rutrum sit amet diam eu, aliquet malesuada eros. Quisque dignissim tortor non purus fringilla finibus. Pellentesque nec dolor augue.</p>
    <p class="bullet" style="top:216px">Donec vestibulum magna est, sed maximus arcu accumsan a. Donec lacus nisl, dignissim a tempor sed, euismod faucibus dolor. Vestibulum diam magna, porttitor vel consequat a, ultricies vitae mauris</p>
    <p class="body" style="top:261px">Lorem ipsum dolor sit amet, consectetur adipiscing elit. Sed ante tortor, rutrum sit amet diam eu, aliquet malesuada eros.<br>Quisque dignissim tortor non purus fringilla finibus. Pellentesque nec dolor augue.<br>Donec vestibulum magna est, sed maximus arcu accumsan a.<br>Donec lacus nisl, dignissim a tempor sed, euismod faucibus dolor. Vestibulum diam magna, porttitor vel consequat a, ultricies vitae mauris</p>
    <p class="sign right" style="right:61px;top:326px">Unterschrift<span>mirko behrens</span></p>
    <div class="foot" style="left:14px">
      <svg width="7" height="9" viewBox="0 0 7 9"><path d="M3.5 0A3.3 3.3 0 0 0 .2 3.3C.2 5.8 3.5 9 3.5 9S6.8 5.8 6.8 3.3A3.3 3.3 0 0 0 3.5 0Zm0 4.6a1.3 1.3 0 1 1 0-2.6 1.3 1.3 0 0 1 0 2.6Z" fill="var(--teal)"/></svg>
      Kiel<br>Strandweg 12
    </div>
    <div class="foot" style="left:116px">
      <svg width="8" height="8" viewBox="0 0 8 8"><path d="M1.6.3 3 1.9 2.3 3c.5 1.1 1.5 2.1 2.6 2.6l1.1-.7 1.6 1.4-.8 1.4C3.3 7.5.5 4.7.3 1.1Z" fill="var(--teal)"/></svg>
      Telefon: +49 431 / 5550123<br>Mobil: +49 170 / 5550124
    </div>
    <div class="foot" style="left:213px">
      <svg width="10" height="7" viewBox="0 0 10 7"><rect x=".5" y=".5" width="9" height="6" fill="none" stroke="var(--teal)" stroke-width=".8"/><path d="M.5.5 5 4 9.5.5" fill="none" stroke="var(--teal)" stroke-width=".8"/></svg>
      E-Mail: post@lumra-osteopathie.de<br>www.lumra-osteopathie.de
    </div>
    <svg class="layer" width="317" height="448" viewBox="0 0 317 448">
      <path d="M0 425 C80 418 160 440 240 432 C280 428 305 418 317 410" fill="none" stroke="var(--blue)" stroke-width="3"/>
    </svg>
  </section>
  <div class="fold" style="left:207px;top:193px"></div>

  <!-- landscape business card, front -->
  <section class="item card-h1">
    <div class="brand" style="left:0;width:225px;top:62px">
      <div class="wordmark" style="font-size:38px">LUMRA</div>
      <div class="tagline" style="font-size:10.6px;margin-top:5px">PRAXIS FÜR OSTEOPATHIE</div>
    </div>
    <p class="web">www.lumra-osteopathie.de</p>
  </section>

  <!-- landscape business card, back -->
  <section class="item card-h2">
    <div class="brand" style="left:18px;top:16px;text-align:left">
      <div class="wordmark" style="font-size:14px;color:var(--faint)">LUMRA</div>
      <div class="tagline" style="font-size:3.8px;color:var(--faint)">PRAXIS FÜR OSTEOPATHIE</div>
    </div>
    <div class="spine" role="img" aria-label="Stilisierte Wirbelsäule als blasse Dekoration" style="left:32px;top:52px;width:30px;height:90px;background:linear-gradient(180deg,rgba(202,216,225,.9),rgba(202,216,225,.4))"></div>
    <p class="name"><small>Dr. med.</small>Mirko Behrens</p>
    <p class="contact">Telefon: +49 431 / 5550123<br>Mobil: +49 170 / 5550124<br>Kiel, Strandweg 12<br>E-Mail: info@lumra-osteopathie.de</p>
    <div class="icons">
      <svg width="6" height="6" viewBox="0 0 8 8"><path d="M1.6.3 3 1.9 2.3 3c.5 1.1 1.5 2.1 2.6 2.6l1.1-.7 1.6 1.4-.8 1.4C3.3 7.5.5 4.7.3 1.1Z" fill="var(--teal)"/></svg>
      <svg width="5" height="7" viewBox="0 0 7 9" style="margin-top:9px"><path d="M3.5 0A3.3 3.3 0 0 0 .2 3.3C.2 5.8 3.5 9 3.5 9S6.8 5.8 6.8 3.3A3.3 3.3 0 0 0 3.5 0Z" fill="var(--teal)"/></svg>
      <svg width="6" height="4" viewBox="0 0 6 4" style="margin-top:8px"><rect width="6" height="4" fill="var(--teal)"/></svg>
    </div>
  </section>

  <!-- letterhead, version B -->
  <section class="item letter letter-b">
    <div class="brand" style="right:22px;top:26px">
      <div class="wordmark" style="font-size:25px">LUMRA</div>
      <div class="tagline" style="font-size:6.8px">PRAXIS FÜR OSTEOPATHIE</div>
    </div>
    <p class="meta" style="top:85px">Betreff:</p>
    <p class="meta" style="top:122px">Sehr geehrte/er</p>
    <p class="body" style="top:139px">Lorem ipsum dolor sit amet, consectetur adipiscing elit. Sed ante tortor, rutrum sit amet diam eu, aliquet malesuada eros. Quisque dignissim tortor non purus fringilla finibus. Pellentesque nec dolor augue. Donec vestibulum magna est, sed maximus arcu accumsan a. Donec lacus nisl, dignissim a tempor sed, euismod faucibus dolor.</p>
    <p class="bullet" style="top:190px">Lorem ipsum dolor sit amet, consectetur adipiscing elit. Sed ante tortor, rutrum sit amet diam eu, aliquet malesuada eros. Quisque dignissim tortor non purus fringilla finibus. Pellentesque nec dolor augue.</p>
    <p class="bullet" style="top:220px">Donec vestibulum magna est, sed maximus arcu accumsan a. Donec lacus nisl, dignissim a tempor sed, euismod faucibus dolor. Vestibulum diam magna, porttitor vel consequat a, ultricies vitae mauris</p>
    <p class="body" style="top:265px">Lorem ipsum dolor sit amet, consectetur adipiscing elit. Sed ante tortor, rutrum sit amet diam eu, aliquet malesuada eros.<br>Quisque dignissim tortor non purus fringilla finibus. Pellentesque nec dolor augue.<br>Donec vestibulum magna est, sed maximus arcu accumsan a.<br>Donec lacus nisl, dignissim a tempor sed, euismod faucibus dolor. Vestibulum diam magna, porttitor vel consequat a, ultricies vitae mauris</p>
    <p class="sign" style="left:53px;top:329px;color:var(--faint)">Unterschrift<span style="color:var(--teal)">Mirko Behrens</span></p>
    <svg class="layer" width="317" height="448" viewBox="0 0 317 448">
      <path d="M0 448 V440 C70 430 110 410 170 390 C230 372 280 372 317 370 V448Z" fill="#f2f3f4"/>
    </svg>
    <p class="fine">Kiel • Strandweg 12 • Telefon: <b>+49 431 / 5550123</b><br>Mobil: +49 170 / 5550124 • E-Mail: post@lumra.de<br><b>Bank:</b> Förde Bank Kiel • <b>Bankleitzahl:</b> 210 500 00<br><b>IBAN:</b> DE21 0000 0000 1111 2222 33 • <b>BIC:</b> FOERDE12<br><b>USt-IdNr.:</b> DE 123456789 • <b>Amtsgericht:</b> Kiel</p>
  </section>
  <div class="fold" style="left:846px;top:193px"></div>

  <!-- envelope 1, front with window -->
  <section class="item env env-1">
    <div class="window"></div>
    <div class="brand" style="left:155px;top:28px">
      <div class="wordmark" style="font-size:16px">LUMRA</div>
      <div class="tagline" style="font-size:4.4px">PRAXIS FÜR OSTEOPATHIE</div>
    </div>
    <svg class="layer" width="245" height="122" viewBox="0 0 245 122">
      <path d="M119 95 C130 88 160 92 200 93 C220 93 235 93 245 92" fill="none" stroke="var(--blue)" stroke-width="4"/>
    </svg>
  </section>

  <!-- envelope 2, back -->
  <section class="item env env-2">
    <svg class="layer" width="245" height="123" viewBox="0 0 245 123">
      <path d="M0 0 V30 H245 V0" fill="#f3f4f5"/>
      <path d="M20 18 H225 L215 28 H30Z" fill="#e3e5e7"/>
      <path d="M0 98 C70 92 130 112 180 105 C215 100 235 85 245 70" fill="none" stroke="var(--blue)" stroke-width="4"/>
    </svg>
    <p class="web" style="left:130px;top:80px">www.lumra-osteopathie.de</p>
  </section>

  <!-- envelope 3, front with window -->
  <section class="item env env-3">
    <div class="window" style="left:23px;top:61px"></div>
    <div class="brand" style="left:152px;top:34px">
      <div class="wordmark" style="font-size:16px">LUMRA</div>
      <div class="tagline" style="font-size:4.4px">PRAXIS FÜR OSTEOPATHIE</div>
    </div>
    <p class="web" style="left:143px;top:88px">www.lumra-osteopathie.de</p>
  </section>

  <!-- envelope 4, back -->
  <section class="item env env-4">
    <svg class="layer" width="244" height="125" viewBox="0 0 244 125">
      <path d="M0 0 V30 H244 V0" fill="#f3f4f5"/>
      <path d="M10 22 H234 L226 30 H18Z" fill="#e3e5e7"/>
    </svg>
    <div class="spine" role="img" aria-label="Stilisierte Wirbelsäule als blaugraue Dekoration" style="left:222px;top:30px;width:12px;height:92px;background:linear-gradient(180deg,rgba(156,180,195,.7),rgba(156,180,195,.35))"></div>
    <p class="line">PRAXIS FÜR OSTEOPATHIE<span>BEHRENS MIRKO</span></p>
  </section>

  <!-- primary logo, colour -->
  <div class="logo-big logo-color">
    <div class="wordmark">LUMRA</div>
    <div class="tagline">PRAXIS FÜR OSTEOPATHIE</div>
  </div>

  <!-- primary logo, greyscale -->
  <div class="logo-big logo-mono">
    <div class="wordmark">LUMRA</div>
    <div class="tagline">PRAXIS FÜR OSTEOPATHIE</div>
  </div>

</main>
</body>
</html>
```